Carpentry and Building Business Card

I'm looking for a business card that is minimalistic and that incorporates the theme of my Velmor logo.
On one side I'd like the VELMOR logo with my details on the other side.
Double sided with curved edges

Target Market(s)

Construction / renovation
Adults

Industry/Entity Type

Tradesman

Contact Information for Business Card

Logo on one side, details on the other

Colors

Designer to choose only greyscale colors for use in the design.

Requirements
Must have
• Nilo Petrakis
VELMOR CONSTRUCT
Carpentry & Building Services
0481236574
Velmorconstruct@brixmail.com
Lic No. 718263D
Nice to have
• Fb and insta icons. @velmorconstruct
Should not have
• No hammer or tool icons please.

No address line.

```html
<!DOCTYPE html>
<html lang="en">
<head>
<meta charset="utf-8">
<title>Velmor Construct – Business Card</title>
<link href="https://fonts.googleapis.com/css2?family=Roboto:wght@300;400;700&display=swap" rel="stylesheet">
<style>
  :root {
    --backdrop: #d9d9d9;
    --card: #ffffff;
    --ink: #111111;
    --ink-soft: #3a3a3a;
    --ink-muted: #555555;
    --card-shadow: rgba(0, 0, 0, 0.18);
  }
  * { margin: 0; padding: 0; box-sizing: border-box; }
  html, body {
    width: 1200px;
    height: 900px;
    overflow: hidden;
    background: var(--backdrop);
    font-family: "Roboto", sans-serif;
    color: var(--ink);
  }
  .sheet {
    width: 1200px;
    height: 900px;
    display: flex;
    flex-direction: column;
    align-items: center;
    justify-content: center;
    gap: 56px;
  }
  .card {
    position: relative;
    width: 620px;
    height: 370px;
    background: var(--card);
    border-radius: 34px;
    box-shadow: 0 10px 28px var(--card-shadow);
  }

  /* Front */
  .card--front {
    display: flex;
    align-items: center;
    justify-content: center;
  }
  .brand {
    display: flex;
    align-items: center;
    gap: 26px;
  }
  .brand__square {
    width: 58px;
    height: 58px;
    border: 3px solid var(--ink);
  }
  .brand__name {
    font-weight: 400;
    font-size: 52px;
    letter-spacing: 0.32em;
    color: var(--ink);
  }

  /* Back */
  .card--back .brand--stacked {
    position: absolute;
    left: 58px;
    bottom: 70px;
    flex-direction: column;
    align-items: center;
    gap: 26px;
  }
  .brand--stacked .brand__square {
    width: 44px;
    height: 44px;
    border-width: 2px;
    border-color: var(--ink-muted);
  }
  .brand--stacked .brand__name {
    font-size: 34px;
    letter-spacing: 0.3em;
  }
  .details {
    position: absolute;
    right: 52px;
    top: 44px;
    text-align: right;
    display: flex;
    flex-direction: column;
    align-items: flex-end;
  }
  .details__name {
    font-weight: 700;
    font-size: 27px;
    color: var(--ink-soft);
    margin-bottom: 8px;
  }
  .details__line {
    font-weight: 300;
    font-size: 14.5px;
    line-height: 1.42;
    color: var(--ink-soft);
  }
  .social {
    display: flex;
    gap: 12px;
    margin-top: 14px;
  }
  .social__item {
    display: flex;
    flex-direction: column;
    align-items: center;
    gap: 3px;
  }
  .social__square {
    width: 26px;
    height: 26px;
    background: var(--ink);
    border-radius: 5px;
  }
  .social__label {
    font-size: 7px;
    font-weight: 400;
    color: var(--ink-muted);
  }
  .social__handle {
    margin-top: 6px;
    font-weight: 400;
    font-size: 15px;
    color: var(--ink-soft);
  }
</style>
</head>
<body>
  <main class="sheet">
    <section class="card card--front" aria-label="Card front">
      <div class="brand">
        <span class="brand__square"></span>
        <span class="brand__name">VELMOR.</span>
      </div>
    </section>

    <section class="card card--back" aria-label="Card back">
      <div class="details">
        <p class="details__name">Nilo Petrakis</p>
        <p class="details__line">VELMOR CONSTRUCT</p>
        <p class="details__line">Carpentry &amp; Building Services</p>
        <p class="details__line">0481236574</p>
        <p class="details__line">Velmorconstruct@brixmail.com</p>
        <p class="details__line">Lic No. 718263D</p>
        <div class="social">
          <div class="social__item">
            <span class="social__square"></span>
            <span class="social__label">Pagelink</span>
          </div>
          <div class="social__item">
            <span class="social__square"></span>
            <span class="social__label">Pictora</span>
          </div>
        </div>
        <p class="social__handle">@velmorconstruct</p>
      </div>

      <div class="brand brand--stacked">
        <span class="brand__square"></span>
        <span class="brand__name">VELMOR.</span>
      </div>
    </section>
  </main>
</body>
</html>
```